Velmora Link needs a brochure review

We are a company operating in more than 10 countries that, since 1972, has the ambitious and innovative objective to stimulate foreign language learning by discovering different countries and cultures, through training courses tailored to individual needs
We need a layout review of our brochure in order to make the content clearer, immediate and appealing and, at the same time, make the layout more modern and young.
The pages we need are: the cover and pages 3, 5, 7, 20, 21, 22, 23, 34, 36, 37. You will find our actual brochure pdf as attachment

Target Market(s)

Students and families, business

Industry/Entity Type

It Company

Requirements
Must have
• The same written information as the actual one.
• Blue and green colours.
• The cover must be simple, elegant and clean but new and effective. In addition to the cover the pages you should review are number :2, 3, 4, 5, 6, 7. Feel free to use new background, images and new layout for the text.

```html
<!DOCTYPE html>
<html lang="it">
<head>
<meta charset="utf-8">
<title>Velmora Link – Sconti prenota prima</title>
<link href="https://fonts.googleapis.com/css2?family=PT+Sans+Narrow:wght@400;700&family=Source+Sans+3:wght@300;400&display=swap" rel="stylesheet">
<style>
  :root{
    --sky-top:#cfe0f3;
    --sky-mid:#a9c6ea;
    --sky-low:#8fb2e6;
    --ink:#1d1d1b;
    --coral:#ee5a5a;
    --orange:#f39c1f;
    --teal:#1d8fbf;
    --green:#10a04a;
    --band-blue:#2aa6df;
    --band-green:#0f8f47;
    --rule:#8aa3bf;
    --white:#ffffff;
  }
  *{margin:0;padding:0;box-sizing:border-box}
  html,body{width:885px;height:1200px;overflow:hidden}
  body{position:relative;font-family:"PT Sans Narrow",sans-serif;color:var(--ink);background:var(--sky-mid)}
  .sky{position:absolute;inset:0;background:
    radial-gradient(ellipse at 30% 20%,rgba(255,255,255,.75),transparent 55%),
    radial-gradient(ellipse at 80% 55%,rgba(255,255,255,.6),transparent 50%),
    radial-gradient(ellipse at 20% 80%,rgba(255,255,255,.55),transparent 45%),
    linear-gradient(180deg,var(--sky-top),var(--sky-mid) 55%,var(--sky-low))}
  .rule{position:absolute;left:290px;width:550px;height:1px;background:var(--rule)}
  .offer{position:absolute;left:0;width:885px}
  .brand{position:absolute;right:610px;text-align:right;font-family:"Source Sans 3",sans-serif;font-weight:400;color:var(--ink);line-height:1.05}
  .brand .tier{display:block;font-size:25px}
  .brand .house{display:block;font-size:38px;letter-spacing:-.5px}
  .copy{position:absolute;left:293px;width:345px;font-size:12.4px;line-height:1.42}
  .badge{position:absolute;left:674px;width:196px;height:196px;border-radius:50%;background:var(--white);
    display:flex;flex-direction:column;align-items:center;justify-content:center;text-align:center}
  .badge .label{font-size:25px;letter-spacing:-.3px;line-height:1}
  .badge .amount{font-family:"Source Sans 3",sans-serif;font-weight:300;font-size:64px;line-height:1;letter-spacing:-2px}
  .badge .deadline{font-size:14px;line-height:1.05;letter-spacing:-.3px}
  .badge .deposit{font-size:13.5px;letter-spacing:-.3px;margin-top:2px}
  .plus .amount,.plus .deposit{color:var(--coral)}
  .aurora .amount,.aurora .deposit{color:var(--orange)}
  .cura .amount{color:var(--teal)}
  .atelier .amount{color:var(--green)}
  .footer-band{position:absolute;top:1160px;height:40px}
  .footer-band.blue{left:0;width:448px;background:var(--band-blue)}
  .footer-band.green{left:448px;width:437px;background:var(--band-green)}
</style>
</head>
<body>
  <div class="sky" role="img" aria-label="Fotografia di cielo azzurro con nuvole bianche"></div>

  <section class="offer plus">
    <div class="brand" style="top:188px"><span class="tier">Aurora Plus</span><span class="house">Velmora Link</span></div>
    <p class="copy" style="top:138px">Prenotando la tua vacanza studio entro questa data, ti garantirai uno sconto di €130 per le destinazioni Europee, o €80 per le destinazioni USA. In regalo per te anche la garanzia Scelta Libera: fino al 28/02/2017 potrai annullare per qualsiasi motivo, senza nessuna penale. Avrai inoltre l’offerta CuraViaggio, del valore di €270, in omaggio (scopri tutti i vantaggi della garanzia a pagina 9). Se hai scelto una destinazione Atelier, in regalo per te il programma Atelier Sport &amp; Dance (del valore di €50 a settimana).</p>
    <div class="badge" style="top:79px"><span class="label">SCONTO</span><span class="amount">€500</span><span class="deadline">Per iscrizioni entro<br>il 20 dicembre 2016</span><span class="deposit">acconto €299</span></div>
  </section>
  <div class="rule" style="top:383px"></div>

  <section class="offer aurora">
    <div class="brand" style="top:468px"><span class="tier">Aurora</span><span class="house">Velmora Link</span></div>
    <p class="copy" style="top:438px">Prenotando la tua vacanza studio entro questa data, avrai uno sconto di €100 per le destinazioni Europee e di €50 per le destinazioni USA. Avrai inoltre l’offerta CuraViaggio, del valore di €270, in omaggio (scopri tutti i vantaggi della garanzia a pagina 9). Se hai scelto una destinazione Atelier, in regalo per te il programma Atelier Sport &amp; Dance (del valore di €50 a settimana).</p>
    <div class="badge" style="top:400px"><span class="label">SCONTO</span><span class="amount">€470</span><span class="deadline">Per iscrizioni entro<br>il 26 gennaio 2017</span><span class="deposit">acconto €299</span></div>
  </section>
  <div class="rule" style="top:624px"></div>

  <section class="offer cura">
    <div class="brand" style="top:690px"><span class="tier">CuraViaggio</span><span class="house">Velmora Link</span></div>
    <p class="copy" style="top:646px">Prenotando la tua vacanza studio entro questa data otterrai gratuitamente la speciale garanzia CuraViaggio, del valore di €100 per ogni settimana di soggiorno. La garanzia ti permette di annullare la vacanza studio fino a 15 giorni prima della partenza, ti protegge contro le oscillazioni dei cambi valutari e ti permette di estendere gratuitamente la polizza USA (del valore di €70). Scopri tutti i vantaggi della garanzia CuraViaggio a pagina 9. Se hai scelto una destinazione Atelier, in regalo per te il programma Atelier Sport &amp; Dance (del valore di €50 a settimana).</p>
    <div class="badge" style="top:633px"><span class="label">SCONTO</span><span class="amount">€370</span><span class="deadline">Per iscrizioni entro<br>il 28 febbraio 2017</span></div>
  </section>
  <div class="rule" style="top:846px"></div>

  <section class="offer atelier">
    <div class="brand" style="top:912px"><span class="tier">Atelier</span><span class="house">Velmora Link</span></div>
    <p class="copy" style="top:905px">Se per la tua vacanza studio hai scelto una destinazione Atelier, prenotando entro questa data avrai in omaggio il programma Atelier Sport o Dance del valore di €50 a settimana e ti garantirai così un risparmio di €100.</p>
    <div class="badge" style="top:852px"><span class="label">SCONTO</span><span class="amount">€100</span><span class="deadline">Per iscrizioni entro<br>il 10 marzo 2017</span></div>
  </section>

  <div class="footer-band blue"></div>
  <div class="footer-band green"></div>
</body>
</html>
```